Podcast Cover Art for Inspiring Fun Show

Title: The Dave R Hour

I am looking for a simple design that includes the following:

1. Picture of me (the one I attached with the background removed) on a simple background (please refer to attachments for ideas).
2. The title done in professional lettering that is easy to read and stands out on the background

Please see attached pictures for:

1) Other podcast art I like
2) Backgrounds that I like
3) A picture of me (please edit out the background)

Target Market(s)

Anyone into personal-development, inspiring content and motivational stories.

Font styles to use
Sans Serif

Colors

Designer to choose colors to be used in the design.

Requirements
Must have
• - Title "The Dave R Hour" in professional lettering that is large and very easy to read
• - Picture of me on the background

```html
<!DOCTYPE html>
<html lang="en">
<head>
<meta charset="utf-8">
<title>The Dave R Hour – Podcast Cover</title>
<link rel="stylesheet" href="https://fonts.googleapis.com/css2?family=Jost:wght@400;500&display=swap">
<style>
  :root {
    --backdrop: #302f52;
    --sunny: #fdd32f;
    --sky: #58b4d9;
    --sky-pale: #acdcec;
    --lilac: #a892ef;
    --navy-disc: #302f52;
    --white: #ffffff;
  }
  * { margin: 0; padding: 0; box-sizing: border-box; }
  html, body {
    width: 1200px; height: 1200px; overflow: hidden;
    background: var(--backdrop);
    font-family: "Jost", sans-serif;
  }
  .cover {
    position: absolute; left: 139px; top: 132px;
    width: 924px; height: 924px;
    box-shadow: 0 14px 40px rgba(0,0,0,0.35);
    overflow: hidden;
  }
  .cover-art { position: absolute; inset: 0; width: 924px; height: 924px; display: block; }
  .title {
    position: absolute; left: 406px; top: 255px;
    width: 440px; height: 440px;
    display: flex; flex-direction: column; align-items: center; justify-content: center;
    color: var(--white); text-align: center;
  }
  .title-the {
    font-size: 30px; font-weight: 500; letter-spacing: 4px; line-height: 1;
    margin-bottom: 12px;
  }
  .title-name, .title-hour {
    font-size: 76px; font-weight: 500; line-height: 1; letter-spacing: 1px;
  }
  .title-hour { margin-top: 6px; }
</style>
</head>
<body>
  <div class="cover">
    <svg class="cover-art" viewBox="0 0 924 924" xmlns="http://www.w3.org/2000/svg">
      <defs>
        <linearGradient id="photoTone" x1="0" y1="0" x2="1" y2="0">
          <stop offset="0" stop-color="#f7e27a"/>
          <stop offset="0.35" stop-color="#d8b56a"/>
          <stop offset="0.55" stop-color="#b39ae8"/>
          <stop offset="1" stop-color="#8a78d8"/>
        </linearGradient>
        <linearGradient id="discBlend" x1="0" y1="0" x2="1" y2="0">
          <stop offset="0" stop-color="#a892ef"/>
          <stop offset="0.45" stop-color="#58b4d9"/>
          <stop offset="1" stop-color="#58b4d9"/>
        </linearGradient>
      </defs>
      <rect class="field" width="924" height="924" fill="var(--sunny)"/>
      <circle class="ring-outer" cx="636" cy="475" r="548" fill="var(--sky-pale)"/>
      <circle class="disc-main" cx="650" cy="475" r="480" fill="url(#discBlend)"/>
      <path class="host-photo" role="img" aria-label="Portrait photo of the host, smiling, tinted yellow and violet"
            d="M0 60 C60 40 140 40 200 60 C300 40 400 90 440 200 C470 300 470 420 450 560 C500 640 560 760 600 924 L0 924 Z"
            fill="url(#photoTone)" opacity="0.9"/>
      <rect class="band" x="840" y="476" width="84" height="32" fill="var(--sky-pale)"/>
      <circle class="title-disc" cx="626" cy="475" r="220" fill="var(--navy-disc)"/>
    </svg>
    <div class="title">
      <span class="title-the">THE</span>
      <span class="title-name">DAVE R</span>
      <span class="title-hour">HOUR</span>
    </div>
  </div>
</body>
</html>
```